Website Home Page Graphics / Banner

We need a Website Home page banner or graphic that is engaging and describes what we do with either words or a graphic story- which is Screen Print & Create promotional products. I love the minimalist design style, but I also want the home page to be descriptive and inviting which I feel it is not. Here is a link to our current website www.brambleinkworks.com Our current tagline is
"Here at Bramble Inkworks, we take a personal approach to screen-printing. Let us support you in creating a product that leaves a lasting impression."
We are sticking with the Black, White, Grey & Green theme as seen on the website. Attached are some photos that inspire me / I would like to replicate in some way on my own home page.

Target Market(s)

Anybody who needs Promotional Products. Although we can relate most to small Businesses and the younger (age 19-35) demographic

Font styles to use
Other font styles liked:
• Heritage, Helvetica Neu - those are my current fonts

Colors
86cfc6
ffffff
c6c6c6
000000
919191

Requirements
Must have
• Engaging Graphic Story that describes in either pictures or words what we do.
Nice to have
• Warm inviting design

```html
<!DOCTYPE html>
<html lang="en">
<head>
<meta charset="utf-8">
<title>Bramble Inkworks – Home Banner</title>
<link href="https://fonts.googleapis.com/css2?family=Oswald:wght@500&family=Questrial&display=swap" rel="stylesheet">
<style>
  :root {
    --teal: #7ccbc5;
    --teal-deep: #5fbcb4;
    --ink: #1c1c1c;
    --charcoal: #333333;
    --ring-grey: #6d6d6d;
    --paper: #ffffff;
    --mist: #e4e4e4;
    --stage: #b3b3b3;
    --photo-light: #f1f1f1;
    --photo-shade: #cfcfcf;
  }
  html, body {
    margin: 0;
    width: 1200px;
    height: 1200px;
    overflow: hidden;
    background: var(--stage);
  }
  .canvas {
    position: relative;
    width: 1200px;
    height: 1200px;
  }
  .banner {
    position: absolute;
    left: 87px;
    top: 389px;
    width: 1030px;
    height: 370px;
    display: block;
  }
  .brand-name {
    font-family: "Questrial", sans-serif;
    font-size: 50px;
    fill: var(--ink);
  }
  .visit-heading {
    font-family: "Oswald", sans-serif;
    font-weight: 500;
    font-size: 74px;
    fill: var(--teal-deep);
  }
  .site-url {
    font-family: "Questrial", sans-serif;
    font-size: 23px;
    fill: var(--paper);
  }
  .tagline {
    font-family: "Questrial", sans-serif;
    font-size: 24px;
  }
  .tagline .dark { fill: var(--charcoal); }
  .tagline .accent { fill: var(--teal-deep); }
</style>
</head>
<body>
<div class="canvas">
  <svg class="banner" viewBox="0 0 1201 431" xmlns="http://www.w3.org/2000/svg">
    <defs>
      <linearGradient id="paperFade" x1="0" y1="0" x2="0" y2="1">
        <stop offset="0" stop-color="#ffffff"/>
        <stop offset="0.55" stop-color="#f6f6f6"/>
        <stop offset="1" stop-color="#e2e2e2"/>
      </linearGradient>
      <linearGradient id="pillFill" x1="0" y1="0" x2="0" y2="1">
        <stop offset="0" stop-color="#3a3a3a"/>
        <stop offset="1" stop-color="#121212"/>
      </linearGradient>
      <radialGradient id="pillShadow" cx="0.5" cy="0.5" r="0.5">
        <stop offset="0" stop-color="#000" stop-opacity="0.45"/>
        <stop offset="1" stop-color="#000" stop-opacity="0"/>
      </radialGradient>
      <radialGradient id="photoTone" cx="0.5" cy="0.45" r="0.6">
        <stop offset="0" stop-color="var(--photo-light)"/>
        <stop offset="1" stop-color="var(--photo-shade)"/>
      </radialGradient>
    </defs>

    <!-- backdrop -->
    <rect class="backdrop" width="1201" height="431" fill="url(#paperFade)"/>
    <rect class="header-field" width="620" height="140" fill="var(--paper)"/>

    <!-- header rules -->
    <rect class="rule-dark" x="0" y="138" width="535" height="7" fill="var(--charcoal)"/>
    <rect class="rule-teal" x="0" y="145" width="525" height="13" fill="var(--teal)"/>

    <!-- chevron divider -->
    <polygon class="chevron-edge" points="615,0 697,0 543,256 768,401 735,401 468,236" fill="var(--teal)"/>
    <polygon class="chevron-core" points="631,0 697,0 543,256 768,401 748,401 486,236" fill="var(--charcoal)"/>

    <!-- footer band -->
    <rect class="footer-band" x="0" y="401" width="1201" height="30" fill="var(--teal)"/>

    <!-- brand name -->
    <text class="brand-name" x="290" y="92" text-anchor="middle">Bramble Inkworks</text>

    <!-- call to action -->
    <text class="visit-heading" x="258" y="257" text-anchor="middle">VISIT US AT</text>
    <ellipse cx="258" cy="362" rx="200" ry="12" fill="url(#pillShadow)"/>
    <rect class="url-pill" x="63" y="281" width="390" height="76" rx="38" fill="url(#pillFill)" stroke="var(--teal)" stroke-width="4"/>
    <text class="site-url" x="258" y="327" text-anchor="middle">www.brambleinkworks.com</text>

    <!-- tagline -->
    <text class="tagline" text-anchor="end">
      <tspan class="dark" x="1151" y="64">Here at Bramble Inkworks, we take a</tspan>
      <tspan class="accent" x="1151" y="94">personal approach to screen-printing</tspan>
      <tspan class="dark" x="1151" y="124">Let us support you in creating a product</tspan>
      <tspan class="accent" x="1151" y="154">that leaves a lasting impression</tspan>
    </text>

    <!-- product showcase -->
    <g class="product-badge">
      <circle cx="662" cy="285" r="88" fill="var(--ring-grey)"/>
      <circle cx="662" cy="285" r="80" fill="var(--teal)"/>
      <circle cx="662" cy="285" r="74" fill="var(--paper)"/>
      <circle cx="662" cy="285" r="68" fill="url(#photoTone)" role="img" aria-label="Photo of a white canvas tote bag with a printed brand stamp"/>
    </g>
    <g class="product-badge">
      <circle cx="861" cy="285" r="88" fill="var(--ring-grey)"/>
      <circle cx="861" cy="285" r="80" fill="var(--teal)"/>
      <circle cx="861" cy="285" r="74" fill="var(--paper)"/>
      <circle cx="861" cy="285" r="68" fill="url(#photoTone)" role="img" aria-label="Photo of a white crewneck sweatshirt with a printed ski team design"/>
    </g>
    <g class="product-badge">
      <circle cx="1059" cy="285" r="88" fill="var(--ring-grey)"/>
      <circle cx="1059" cy="285" r="80" fill="var(--teal)"/>
      <circle cx="1059" cy="285" r="74" fill="var(--paper)"/>
      <circle cx="1059" cy="285" r="68" fill="url(#photoTone)" role="img" aria-label="Photo of a folded white t-shirt with a printed monogram"/>
    </g>
  </svg>
</div>
</body>
</html>
```